Personal Brand (Influencer) Website

I'm looking for a brand new website design for a youtuber/influencer Dalton Merriweather.

I'm looking for a sleek design that is visually appealing while still maintaining full functionality and user experience.

Here is our current website: http://daltonmerriweatherhub.example/

I want to combine some of the best elements and designs from the following websites.

https://www.kelvinrastowski.example/
https://www.osmanferrie.example/
https://nedpalworth.example/
https://www.wadeclemmont.example/
http://daltonmerriweatherhub.example/
http://www.ravifenn.example/

Here are the different tabs that I would need designed as well as the main page:

Home Page (main page)
Blogs
My story (about me)
Top 100 book list
Contact

Here are several links and social media handles for you to get a better gauge on the branding of Dalton Merriweather:
https://www.vidstreamer.example/channel/QXpo3r7t2k-M9hhPPz_WSt4q
https://surge-kickoff.example/marketplace-blog/uncategorized/dalton-merriweather-entrepreneur-winning-marketplace-follow-data-ep-17/
https://daltonlisten2.pagepipes.example/optin-48207315
https://www.snapgallery.example/officialdaltonmerriweather/

```html
<!DOCTYPE html>
<html lang="en">
<head>
<meta charset="utf-8">
<title>Dalton Merriweather — Speaker, Inventor, Bio-Hacker</title>
<link rel="stylesheet" href="https://fonts.googleapis.com/css2?family=Permanent+Marker&family=Poppins:wght@400;500;600;700&display=swap">
<style>
:root{
  --canvas:#dfe6ea;
  --blue:#3fb7ea;
  --blue-deep:#1f8fe0;
  --ink:#1d2229;
  --muted:#7a828a;
  --white:#ffffff;
  --night:#1b2a3c;
  --hero-a:#2f4f73;
  --hero-b:#6f8aa6;
  --hero-c:#2c3b2a;
  --mist:#eef1f3;
}
*{box-sizing:border-box;margin:0;padding:0}
html,body{width:1200px;height:3502px;overflow:hidden}
body{background:var(--canvas);font-family:"Poppins",sans-serif;color:var(--ink);position:relative}
.page{position:absolute;left:100px;top:90px;width:1000px;height:3322px;background:var(--white);overflow:hidden;box-shadow:0 10px 40px rgba(30,50,70,.12)}
.section{position:absolute;left:0;width:1000px;overflow:hidden}
.abs{position:absolute}
.marker{font-family:"Permanent Marker",cursive;letter-spacing:1px}
.btn{position:absolute;display:flex;align-items:center;justify-content:center;font-size:10px;font-weight:600;letter-spacing:2px;text-transform:uppercase}
.btn-solid{background:var(--blue);color:var(--white)}
.btn-line{border:1px solid rgba(255,255,255,.7);color:var(--white)}
.photo{position:absolute}

/* hero */
.hero{top:0;height:585px;background:linear-gradient(180deg,var(--hero-a) 0%,#4d6c8d 30%,var(--hero-b) 48%,#5d6a60 66%,var(--hero-c) 100%)}
.brand{left:40px;top:28px;display:flex;align-items:center;gap:8px;color:var(--white);font-weight:700;font-size:15px;letter-spacing:1px}
.brand-mark{width:14px;height:14px;background:var(--blue)}
.nav{right:250px;top:34px;display:flex;gap:36px;color:var(--white);font-size:11px;font-weight:500;letter-spacing:1px}
.nav .active{color:var(--blue)}
.hero-title{left:0;width:1000px;top:215px;text-align:center;color:var(--white);font-size:68px}
.hero-sub{left:0;width:1000px;top:312px;text-align:center;color:var(--white);font-size:22px;font-weight:600}
.hero-bar{left:0;top:500px;width:1000px;height:85px;background:rgba(10,18,28,.55)}
.hero-bar p{position:absolute;left:85px;top:30px;color:var(--white);font-size:17px;font-weight:600}

/* story */
.story{top:585px;height:506px;background:var(--white)}
.label{color:var(--blue);font-size:10px;font-weight:600;letter-spacing:2px;text-transform:uppercase}
.story h2{position:absolute;left:85px;top:120px;width:340px;font-size:24px;line-height:1.3;font-weight:600}
.story .copy{position:absolute;left:85px;width:360px;font-size:12px;line-height:1.7;color:var(--muted)}

/* courses */
.courses{top:1091px;height:503px;background:linear-gradient(180deg,#3a4650 0%,#222b33 45%,#1e2a2e 75%,#3b3e3a 100%);color:var(--white);text-align:center}
.courses h2{position:absolute;left:0;width:1000px;top:110px;font-size:64px;font-weight:400}
.courses h3{position:absolute;left:0;width:1000px;top:205px;font-size:24px;font-weight:600}
.courses .copy{position:absolute;left:250px;width:500px;top:255px;font-size:12px;line-height:1.8}

/* posts */
.posts{top:1594px;height:582px;background:linear-gradient(180deg,#f4f6f7 0%,#e3e8eb 60%,#f1f3f4 100%)}
.center-title{position:absolute;left:0;width:1000px;text-align:center;color:var(--blue-deep);font-size:42px;font-weight:400}
.center-sub{position:absolute;left:0;width:1000px;text-align:center;font-size:18px;font-weight:600}
.post{position:absolute;top:165px;width:255px}
.post-thumb{height:200px;position:relative}
.post-tag{position:absolute;left:8px;bottom:-10px;background:var(--blue);color:var(--white);font-size:9px;font-weight:600;letter-spacing:1.5px;padding:5px 14px}
.play{position:absolute;left:50%;top:50%;transform:translate(-50%,-50%)}
.post h4{margin-top:26px;font-size:15px;font-weight:500;line-height:1.4;color:var(--ink)}

/* books */
.books{top:2176px;height:706px;background:var(--white)}
.book{position:absolute}
.book-caption{position:absolute;width:160px;text-align:center;font-size:13px;line-height:1.4}
.price{display:block;margin-top:6px;color:var(--blue);font-weight:600}

/* footer */
.footer{top:2882px;height:440px;background:linear-gradient(180deg,#eef1f3 0%,#e6ebee 55%,#f7f8f9 75%,#dfe5e9 100%);text-align:center}
.signup{left:240px;top:148px;width:520px;height:38px;display:flex;border-bottom:1px solid #b9c2c8}
.signup span{flex:1;text-align:left;padding:11px 14px;font-size:12px;color:var(--muted);background:var(--white)}
.signup b{width:150px;background:var(--blue);color:var(--white);font-size:10px;letter-spacing:2px;display:flex;align-items:center;justify-content:center;font-weight:600}
.footer .mail{left:0;width:1000px;top:220px;font-size:17px;color:#4d555c}
.social{left:437px;top:262px;display:flex;gap:18px}
.copyright{left:0;width:1000px;top:330px;font-size:9px;letter-spacing:2px;color:#5f676e}
</style>
</head>
<body>
<main class="page">

  <section class="section hero">
    <div class="abs brand"><span class="brand-mark"></span>DALTON MERRIWEATHER</div>
    <nav class="abs nav"><span class="active">HOME</span><span>MY STORY</span><span>MY BOOK</span><span>BLOG</span></nav>
    <div class="btn btn-solid" style="left:770px;top:24px;width:140px;height:34px">Contact Me!</div>
    <div class="photo" role="img" aria-label="Mountain valley landscape under a cloudy sky" style="left:0;top:0;width:1000px;height:585px;background:radial-gradient(ellipse at 50% 40%,rgba(200,215,230,.35),transparent 60%)"></div>
    <h1 class="abs marker hero-title">DALTON MERRIWEATHER</h1>
    <p class="abs hero-sub">Speaker, Inventor, Bio-Hacker and Positive Thinker.</p>
    <div class="abs hero-bar">
      <p>Sign Up for a Complimentary Results Coaching Session Today!</p>
      <div class="btn btn-line" style="left:770px;top:26px;width:140px;height:32px">Subscribe Me!</div>
    </div>
  </section>

  <section class="section story">
    <p class="abs label" style="left:85px;top:95px">My Story</p>
    <h2>Dalton is a bio-hacker, YouTuber, husband, and llama lover.</h2>
    <p class="copy" style="top:240px">Dalton Merriweather is a 7 figure Ecommerce Entrepreneur, Speaker, Inventor, Bio-Hacker, and Positive thinker. He believes the world is getting better every day.</p>
    <p class="copy" style="top:305px">Dalton went from 0 to 3 Million in 9 Months selling Eclipse Glasses on Marketplace. He also proposed to his wife in Outer Space. He is not your typical person ...</p>
    <div class="btn btn-solid" style="left:85px;top:385px;width:130px;height:32px">Discover More</div>
    <div class="abs" role="img" aria-label="Handwritten signature" style="left:240px;top:378px;width:120px;height:46px;background:linear-gradient(90deg,rgba(29,34,41,.12),rgba(29,34,41,.04))"></div>
    <div class="photo" role="img" aria-label="Portrait of Dalton in a cap with a backpack in the mountains" style="left:500px;top:0;width:500px;height:506px;background:linear-gradient(160deg,#5b6a74 0%,#8a8672 35%,#b3905f 60%,#6e5a44 100%)"></div>
  </section>

  <section class="section courses">
    <div class="photo" role="img" aria-label="Dark mountain lake landscape" style="left:0;top:0;width:1000px;height:503px;background:radial-gradient(ellipse at 50% 55%,rgba(90,110,120,.35),transparent 65%)"></div>
    <h2 class="marker">FEATURED COURSES</h2>
    <h3>The First Free Marketplace Private Label Course</h3>
    <p class="copy">I am giving away everything that I know for free.<br>Myself &amp; the top Marketplace sellers will be teaching you everything that you need to know about creating &amp; managing a thriving Marketplace Business so that you can live your life on your terms.</p>
    <div class="btn btn-line" style="left:430px;top:375px;width:140px;height:32px">Sign Up Here!</div>
  </section>

  <section class="section posts">
    <h2 class="center-title marker" style="top:65px">RECENT POSTS</h2>
    <p class="center-sub" style="top:118px">Keep Going. Start Chasing The Passion.</p>

    <article class="post" style="left:85px">
      <div class="post-thumb photo" role="img" aria-label="Video still of Dalton talking in a studio with colored lights" style="position:relative;background:linear-gradient(135deg,#3a2f55 0%,#5a4f6e 45%,#2b3a55 100%)">
        <svg class="play" width="40" height="40" viewBox="0 0 40 40"><circle cx="20" cy="20" r="20" fill="#fff"/><path d="M16 12 L28 20 L16 28 Z" fill="#1d2229"/></svg>
        <span class="post-tag">BLOG</span>
      </div>
      <h4>Surge Kickoff Product Discovery Destroys Canopy Finder Niche Hunter?</h4>
    </article>

    <article class="post" style="left:373px">
      <div class="post-thumb photo" role="img" aria-label="Video still of Dalton outdoors among green trees" style="position:relative;background:linear-gradient(135deg,#6e8a5a 0%,#b08f7a 50%,#4f6a45 100%)">
        <svg class="play" width="40" height="40" viewBox="0 0 40 40"><circle cx="20" cy="20" r="20" fill="#fff"/><path d="M16 12 L28 20 L16 28 Z" fill="#1d2229"/></svg>
        <span class="post-tag">PODCASTS</span>
      </div>
      <h4>How Much MONEY Do You NEED To Get Started On MARKETPLACE? Part (1) $500 Approach</h4>
    </article>

    <article class="post" style="left:661px">
      <div class="post-thumb photo" role="img" aria-label="Video still of Dalton in a room lit pink and blue" style="position:relative;background:linear-gradient(135deg,#2a3550 0%,#6a4a68 50%,#2c5570 100%)">
        <svg class="play" width="40" height="40" viewBox="0 0 40 40"><circle cx="20" cy="20" r="20" fill="#fff"/><path d="M16 12 L28 20 L16 28 Z" fill="#1d2229"/></svg>
        <span class="post-tag">BLOG</span>
      </div>
      <h4>Marketplace Seller PRODUCT RESEARCH 7 Failed Products in a row! Lessons I Learned (5th did $6,900,000)</h4>
    </article>

    <div class="btn btn-solid" style="left:430px;top:475px;width:140px;height:32px">View All Posts</div>
  </section>

  <section class="section books">
    <div class="photo" role="img" aria-label="Portrait of Dalton smiling outdoors with a backpack" style="left:85px;top:40px;width:310px;height:430px;background:linear-gradient(170deg,#c9d0d2 0%,#b6a98f 45%,#8a6a4c 80%,#5c4636 100%)"></div>
    <h2 class="abs marker" style="left:450px;top:45px;color:var(--blue-deep);font-size:40px;font-weight:400">MY BOOKS</h2>
    <p class="abs" style="left:450px;top:97px;font-size:20px;font-weight:600">Read My Books and Start a New Life!</p>
    <p class="abs label" style="left:450px;top:133px;font-size:9px">Book by <span style="color:var(--ink)">Dalton Merriweather</span></p>

    <div class="book" style="left:345px;top:225px;width:170px;height:250px;background:var(--white);box-shadow:0 8px 24px rgba(0,0,0,.15)">
      <div role="img" aria-label="Book cover with a warm painted illustration" style="position:absolute;left:18px;top:18px;width:134px;height:214px;background:linear-gradient(180deg,#e9c36a 0%,#c9873c 50%,#8a4a2a 100%)"></div>
    </div>
    <div class="book" role="img" aria-label="Dark book cover with bold white title" style="left:550px;top:245px;width:155px;height:210px;background:linear-gradient(180deg,#1b1b1b,#2e2e2e)"></div>
    <div class="book" role="img" aria-label="Navy book cover with white title lettering" style="left:745px;top:245px;width:155px;height:210px;background:linear-gradient(180deg,#1e2f55,#2a3f6e)"></div>
    <svg class="abs" style="left:940px;top:340px" width="22" height="22" viewBox="0 0 22 22"><path d="M8 4 L15 11 L8 18" fill="none" stroke="#3fb7ea" stroke-width="2"/></svg>

    <p class="book-caption" style="left:350px;top:495px">Lorem Ipsum is simply dummy text<span class="price">€25.00</span></p>
    <p class="book-caption" style="left:548px;top:495px">Lorem Ipsum is simply dummy text<span class="price">€35.00</span></p>
    <p class="book-caption" style="left:742px;top:495px">Lorem Ipsum is simply dummy text<span class="price">€45.00</span></p>

    <div class="btn" style="left:435px;top:610px;width:130px;height:30px;color:var(--blue);border-top:1px solid var(--blue);border-bottom:1px solid var(--blue);font-size:9px">View All Books</div>
  </section>

  <footer class="section footer">
    <div class="photo" role="img" aria-label="Soft white clouds below the horizon" style="left:0;top:250px;width:1000px;height:190px;background:radial-gradient(ellipse at 30% 70%,#ffffff 0%,rgba(255,255,255,0) 55%),radial-gradient(ellipse at 75% 60%,#ffffff 0%,rgba(255,255,255,0) 55%)"></div>
    <h2 class="center-title marker" style="top:65px">NEWSLETTER</h2>
    <div class="abs signup"><span>name@email.com</span><b>SUBSCRIBE ME!</b></div>
    <p class="abs mail">daltonmerriweather@mailbox.example</p>
    <div class="abs social">
      <svg width="34" height="34" viewBox="0 0 34 34"><circle cx="17" cy="17" r="16" fill="none" stroke="#4d555c" stroke-width="1.5"/></svg>
      <svg width="34" height="34" viewBox="0 0 34 34"><circle cx="17" cy="17" r="16" fill="#4d555c"/></svg>
      <svg width="34" height="34" viewBox="0 0 34 34"><circle cx="17" cy="17" r="16" fill="none" stroke="#4d555c" stroke-width="1.5"/></svg>
    </div>
    <p class="abs copyright">© 2018 DALTON MERRIWEATHER</p>
  </footer>

</main>
</body>
</html>
```